website homepage design sample for tolvenra.com.au

Hello, I am looking to update my website to be simpler and more modern and to include space for my upcoming online courses. Please review my website tolvenra.com.au for an idea of me as a male psychologist, as well as my services. I would like it to be NOT too feminine. Target market is Men and women interested in couselling, life coaching, and online courses about relationships. Id like to keep the beach theme if possible but I am open to better ideas. thank you!

please see tolvenra.com.au for my current wordpress website.

Target Market(s)

Men and Women

Industry/Entity Type

psychology

Number of Pages Required

1 page

Requirements
Must have
• An "Online Training" Menu that includes links to "Map your Daybreak" , "Harbour and Lantern Journey," "Quiet Orchard Course" "Where Did All The Kites Go" "Gathering Willow Moments"

```html
<!DOCTYPE html>
<html lang="en">
<head>
<meta charset="utf-8">
<title>Tolvenra – Psychology Solutions</title>
<link href="https://fonts.googleapis.com/css2?family=Poppins:wght@300;400;500;600&display=swap" rel="stylesheet">
<style>
:root{
  --teal:#239fc0;
  --teal-dark:#1b87a4;
  --sand:#ecdcc3;
  --ink:#1d1d1d;
  --text:#444;
  --pale:#eef7fa;
  --footer:#3b3b3b;
}
*{margin:0;padding:0;box-sizing:border-box}
html,body{width:1200px;height:5343px;overflow:hidden}
body{position:relative;font-family:'Poppins',sans-serif;color:var(--ink);background:#fff}
.abs{position:absolute}
.topbar{left:0;top:0;width:1200px;height:36px;background:var(--teal);color:#fff;font-size:13px;text-align:center;line-height:36px}
.nav{left:0;top:36px;width:1200px;height:78px;background:#fff;display:flex;align-items:center}
.brand{position:absolute;left:68px;top:22px;display:flex;align-items:center;gap:8px;font-weight:600;font-size:15px;color:var(--teal)}
.brand i{width:22px;height:22px;border-radius:50%;background:var(--teal);display:block}
.menu{position:absolute;left:433px;top:28px;display:flex;gap:30px;font-size:12px;text-transform:uppercase;color:#333}
.menu .on{color:var(--teal);border-bottom:2px solid var(--teal);padding-bottom:4px}
.btn{display:inline-block;background:var(--teal);color:#fff;border-radius:30px;font-weight:500;text-transform:uppercase}
.book{position:absolute;left:1009px;top:17px;width:125px;height:42px;line-height:42px;text-align:center;font-size:13px}
.hero{left:0;top:114px;width:1200px;height:706px;background:linear-gradient(100deg,#6a5848 0%,#b99979 35%,#f3e6d6 65%,#fbf3ea 100%);clip-path:polygon(0 0,100% 0,100% 82%,0 100%)}
.hero h1{position:absolute;left:558px;top:70px;font-size:78px;font-weight:400;color:var(--teal);letter-spacing:-1px}
.hero h1 .dark{color:var(--ink)}
.hero .tag{position:absolute;left:560px;top:158px;font-size:26px;font-weight:500}
.hero .next{position:absolute;left:560px;top:206px;width:482px;height:34px;background:var(--teal);color:#fff;font-size:17px;font-weight:500;text-align:center;line-height:34px}
.hero p{position:absolute;left:565px;top:274px;width:485px;font-size:14.5px;line-height:28px;color:#333}
.hero .cta{position:absolute;left:563px;top:428px;width:212px;height:46px;line-height:46px;text-align:center;font-size:14px}
.dots{position:absolute;left:580px;top:574px;display:flex;gap:6px}
.dots i{width:9px;height:9px;border-radius:50%;background:#fff;opacity:.6}
.dots i:first-child{opacity:1}
.heading{left:0;width:1200px;text-align:center;font-size:54px;font-weight:400}
.heading span{display:inline-flex;align-items:center;gap:14px}
.heading span::before,.heading span::after{content:"";width:84px;height:2px;background:var(--teal)}
.sub{left:0;top:955px;width:1200px;text-align:center;color:var(--teal);font-size:24px;font-weight:500}
.lead{left:270px;top:998px;width:660px;text-align:center;font-size:14px;line-height:26px;color:#444}
.arrow{width:42px;height:42px;border-radius:50%;display:flex;align-items:center;justify-content:center}
.arrow.prev{background:#e0e0e0}
.arrow.next{background:var(--teal)}
.service{width:200px;text-align:center;top:1089px}
.service .ring{width:136px;height:136px;margin:0 auto;border-radius:50%;background:linear-gradient(120deg,var(--teal) 25%,var(--sand) 100%)}
.service p{margin-top:30px;font-size:19px;font-weight:500;line-height:23px}
.aboutband{left:0;top:1389px;width:1200px;height:700px;background:var(--pale);clip-path:polygon(0 0,100% 12%,100% 100%,0 100%)}
.about h2{position:absolute;left:125px;top:1536px;font-size:46px;font-weight:400;display:flex;align-items:center;gap:16px}
.about h2::after,.side-h1::after{content:"";width:82px;height:2px;background:var(--teal)}
.about p{position:absolute;left:125px;top:1630px;width:515px;font-size:13.5px;line-height:26.6px;color:#444}
.about .more{position:absolute;left:125px;top:1856px;width:134px;height:42px;line-height:42px;text-align:center;font-size:12.5px}
.portrait{left:708px;top:1556px;width:370px;height:370px;border-radius:50%;border:10px solid var(--teal);border-right-color:var(--sand);border-bottom-color:var(--sand);padding:12px}
.portrait div{width:100%;height:100%;border-radius:50%;background:linear-gradient(160deg,#d9d5d3,#b7a59a)}
.card{top:2295px;width:302px;height:363px;display:flex;align-items:flex-end;justify-content:center;color:#fff;font-weight:600;font-size:17px;text-transform:uppercase;padding-bottom:38px;text-align:center}
.card.mid{align-items:center;padding:0 40px 90px;background:linear-gradient(160deg,#3fb2cd,#1f97b8);font-size:20px;line-height:30px}
.lightband{left:0;top:2757px;width:1200px;height:950px;background:linear-gradient(#eef7fa,#fff);clip-path:polygon(0 0,100% 4%,100% 100%,0 100%)}
.sunset{left:135px;top:2923px;width:360px;height:408px;border-radius:16px;background:linear-gradient(#b890b3 0%,#e8a887 45%,#f1c06b 60%,#3b3b45 100%)}
.side-h{left:555px;top:2915px;font-size:48px;font-weight:400;line-height:58px}
.side-h1{display:flex;align-items:center;gap:16px}
.side-p{left:555px;top:3105px;width:515px;font-size:13.5px;line-height:26.8px;color:#444}
.challenges{left:137px;top:3381px;width:935px;height:226px;background:var(--teal);border-radius:24px;color:#fff;font-size:15px}
.challenges ul{position:absolute;top:54px;list-style:none;line-height:31px}
.challenges li{display:flex;align-items:center;gap:12px}
.online{position:absolute;left:645px;top:102px;width:160px;height:44px;line-height:44px;background:#fff;color:#222;border-radius:30px;text-align:center;font-size:14px;font-weight:500}
.step{width:152px;height:152px;top:3854px;border-radius:50%;border:3px solid var(--teal);padding:6px}
.step div{width:100%;height:100%;border-radius:50%;background:linear-gradient(100deg,var(--teal) 35%,var(--sand));color:#fff;font-size:66px;font-weight:300;display:flex;align-items:center;justify-content:center}
.step-t{top:4025px;width:310px;text-align:center;font-size:24px;line-height:35px;color:#222}
.worth{left:0;top:4322px;width:1200px;height:676px;background:linear-gradient(100deg,#2f6c8b 0%,#5a9bb2 40%,#e9a65a 72%,#7b6a5b 100%);clip-path:polygon(0 0,100% 14%,100% 100%,0 100%)}
.worth h2{position:absolute;left:62px;top:152px;font-size:56px;font-weight:400;color:#fff;display:flex;align-items:center;gap:14px}
.worth h2::after{content:"";width:82px;height:2px;background:#fff}
.worth h3{position:absolute;left:68px;top:253px;font-size:31px;font-weight:500;color:#fff;line-height:52px}
.worth .ebook{position:absolute;left:68px;top:393px;width:508px;height:68px;background:#fff;border-radius:40px;font-size:20px;font-weight:600;display:flex;align-items:center;justify-content:center;gap:14px}
.footer{left:0;top:4998px;width:1200px;height:268px;background:var(--footer);color:#fff}
.badge{position:absolute;left:84px;width:118px;height:58px;border-radius:4px;background:#fff}
.col{position:absolute;top:44px;font-size:11.5px}
.col h4{font-size:15px;font-weight:500;margin-bottom:26px}
.col li{list-style:none;line-height:23.5px;display:flex;align-items:center;gap:8px}
.contact li{align-items:flex-start;line-height:15px;margin-bottom:20px}
.ico{width:22px;height:22px;background:var(--teal);border-radius:3px;flex:none}
.field{width:196px;height:30px;background:#fff;margin-top:16px}
.sub-btn{width:96px;height:28px;background:var(--teal);margin-top:10px;font-size:10px;text-align:center;line-height:28px}
.bottom{left:0;top:5266px;width:1200px;height:77px;background:var(--teal);color:#fff;font-size:12px}
.social{position:absolute;left:1013px;top:26px;display:flex;gap:8px}
.social i{width:24px;height:24px;background:#fff;border-radius:3px;display:block}
</style>
</head>
<body>

<div class="abs topbar">SELF ESTEEM COURSE only $47</div>

<header class="abs nav">
  <div class="brand"><i></i>TOLVENRA</div>
  <nav class="menu">
    <span class="on">Home</span><span>About Us</span><span>Services &amp; Fees ▾</span><span>Online Training ▾</span><span>Blog</span><span>Contact</span>
  </nav>
  <span class="btn book">Bookings</span>
</header>

<section class="abs hero" role="img" aria-label="Man meditating cross-legged on a beach pier at sunrise">
  <h1>TOLV<span class="dark">enra</span></h1>
  <div class="tag">Psychology Solutions + Your Choices</div>
  <div class="next">NEXT AVAILABLE APPOINTMENT: WITHIN 7 DAYS</div>
  <p>At Tolvenra, we are focused on your mental wellness. Tolvenra is open to anyone looking for an Online or Gold Coast Psychologist to help them overcome barriers and find fulfilment in their lives.</p>
  <span class="btn cta">Book Appointment</span>
  <div class="dots"><i></i><i></i><i></i></div>
</section>

<h2 class="abs heading" style="top:866px"><span>Our Services</span></h2>
<div class="abs sub">Psychological Counselling</div>
<p class="abs lead">Tolvenra can provide assistance in the assessment and treatment of psychological and mental health problems related to:</p>

<div class="abs arrow prev" style="left:49px;top:1154px"><svg width="12" height="12" viewBox="0 0 12 12"><path d="M8 1 3 6l5 5" stroke="#fff" stroke-width="2" fill="none"/></svg></div>
<div class="abs arrow next" style="left:1109px;top:1154px"><svg width="12" height="12" viewBox="0 0 12 12"><path d="M4 1l5 5-5 5" stroke="#fff" stroke-width="2" fill="none"/></svg></div>

<div class="abs service" style="left:102px"><div class="ring" role="img" aria-label="Anxiety icon"></div><p>Anxiety and<br>Depression</p></div>
<div class="abs service" style="left:301px"><div class="ring" role="img" aria-label="Trauma icon"></div><p>Trauma</p></div>
<div class="abs service" style="left:502px"><div class="ring" role="img" aria-label="Dating icon"></div><p>Dating and<br>Relationships</p></div>
<div class="abs service" style="left:702px"><div class="ring" role="img" aria-label="Self esteem icon"></div><p>Self Esteem</p></div>
<div class="abs service" style="left:896px"><div class="ring" role="img" aria-label="Work stress icon"></div><p>Work Related<br>Stress</p></div>

<div class="abs aboutband"></div>
<section class="about">
  <h2>About Us</h2>
  <p>Daniel Hartwell has over 13 years experience as a registered psychologist and has been training in psychology since 1997. Daniel strives to provide best-practice, ethical, professional, warm, friendly and non-judgemental counseling and therapy services to clients under Carewell Mental Health Plans. Daniel provides experienced CBT, psychodynamic and Trauma Therapy and is an Advanced Eye Movement Desensitisation and Reprocessing (EMDR) Therapist.</p>
  <span class="btn more">Know More</span>
</section>
<div class="abs portrait"><div role="img" aria-label="Portrait photo of the psychologist"></div></div>

<h2 class="abs heading" style="top:2150px"><span>Online Training</span></h2>
<div class="abs arrow prev" style="left:49px;top:2454px"><svg width="12" height="12" viewBox="0 0 12 12"><path d="M8 1 3 6l5 5" stroke="#fff" stroke-width="2" fill="none"/></svg></div>
<div class="abs arrow next" style="left:1109px;top:2454px"><svg width="12" height="12" viewBox="0 0 12 12"><path d="M4 1l5 5-5 5" stroke="#fff" stroke-width="2" fill="none"/></svg></div>
<div class="abs card" style="left:120px;background:linear-gradient(#cfc4b6,#6f665d)" role="img" aria-label="Counselling session photo">Map your Daybreak</div>
<div class="abs card mid" style="left:448px">Harbour and Lantern Journey</div>
<div class="abs card" style="left:777px;background:linear-gradient(90deg,#3b3633,#c9c3bc)" role="img" aria-label="Confident man pointing photo">Quiet Orchard Course</div>

<div class="abs lightband"></div>
<div class="abs sunset" role="img" aria-label="Silhouette of a woman with open arms at sunset by the sea"></div>
<h2 class="abs side-h"><span class="side-h1">Tolvenra</span>by Daniel Hartwell</h2>
<div class="abs side-p">
  <p>Congratulations on taking the first step to overcoming your barriers and being who you want to be. At Tolvenra, we are focused on your mental wellness. Tolvenra is open to anyone looking for a Gold Coast Psychologist or online therapist to help them overcome barriers and find fulfilment in their lives. We also offer online programs.</p>
  <p style="margin-top:26px">Daniel, your Gold Coast Psychologist, can help you through a variety of challenges:</p>
</div>

<section class="abs challenges">
  <ul style="left:106px">
    <li><svg width="16" height="14" viewBox="0 0 16 14"><path d="M2 7l4 4 8-9" stroke="#fff" stroke-width="2.4" fill="none"/></svg>Depression</li>
    <li><svg width="16" height="14" viewBox="0 0 16 14"><path d="M2 7l4 4 8-9" stroke="#fff" stroke-width="2.4" fill="none"/></svg>Relationship problems</li>
    <li><svg width="16" height="14" viewBox="0 0 16 14"><path d="M2 7l4 4 8-9" stroke="#fff" stroke-width="2.4" fill="none"/></svg>Personal development</li>
    <li><svg width="16" height="14" viewBox="0 0 16 14"><path d="M2 7l4 4 8-9" stroke="#fff" stroke-width="2.4" fill="none"/></svg>Tauma and EMDR</li>
  </ul>
  <ul style="left:392px">
    <li><svg width="16" height="14" viewBox="0 0 16 14"><path d="M2 7l4 4 8-9" stroke="#fff" stroke-width="2.4" fill="none"/></svg>Anxiety</li>
    <li><svg width="16" height="14" viewBox="0 0 16 14"><path d="M2 7l4 4 8-9" stroke="#fff" stroke-width="2.4" fill="none"/></svg>ADHD</li>
    <li><svg width="16" height="14" viewBox="0 0 16 14"><path d="M2 7l4 4 8-9" stroke="#fff" stroke-width="2.4" fill="none"/></svg>Anger management</li>
    <li><svg width="16" height="14" viewBox="0 0 16 14"><path d="M2 7l4 4 8-9" stroke="#fff" stroke-width="2.4" fill="none"/></svg>Life Coaching</li>
  </ul>
  <span class="online">BOOK ONLINE</span>
</section>

<h2 class="abs heading" style="top:3716px"><span>Tolvenra Objectives</span></h2>
<div class="abs step" style="left:123px"><div>1</div></div>
<div class="abs step" style="left:511px"><div>2</div></div>
<div class="abs step" style="left:888px"><div>3</div></div>
<svg class="abs" style="left:300px;top:3880px" width="190" height="50" viewBox="0 0 190 50"><path d="M4 36 Q95 -14 180 40" stroke="var(--teal)" stroke-width="2.5" stroke-dasharray="7 6" fill="none"/><path d="M170 32l10 9 2-13" stroke="var(--teal)" stroke-width="2.5" fill="none"/></svg>
<svg class="abs" style="left:686px;top:3880px" width="190" height="50" viewBox="0 0 190 50"><path d="M4 36 Q95 -14 180 40" stroke="var(--teal)" stroke-width="2.5" stroke-dasharray="7 6" fill="none"/><path d="M170 32l10 9 2-13" stroke="var(--teal)" stroke-width="2.5" fill="none"/></svg>
<p class="abs step-t" style="left:44px">Alleviate distress.</p>
<p class="abs step-t" style="left:432px">Take the next step in helping you create a fulfilling, meaningful and enjoyable life through coaching and positive psychology.</p>
<p class="abs step-t" style="left:809px">Learn, implement and habitualise advanced performance strategies for lasting change.</p>

<section class="abs worth" role="img" aria-label="Person meditating on the shore at sunset">
  <h2>Finding Self Worth</h2>
  <h3>Wondering where to start?<br>Watch our free Self Worth Webinar</h3>
  <span class="ebook">5 STEPS CLOSER TO SELF ESTEEM ONLY $47 <svg width="32" height="12" viewBox="0 0 32 12"><path d="M0 6h29M24 1l6 5-6 5" stroke="#111" stroke-width="2" fill="none"/></svg></span>
</section>

<footer class="abs footer">
  <div class="badge" style="top:82px" role="img" aria-label="Partner badge"></div>
  <div class="badge" style="top:150px" role="img" aria-label="Certification badge"></div>
  <div class="col" style="left:280px"><h4>Quick Links</h4><ul>
    <li>✓ About Us</li><li>✓ Services &amp; Fees</li><li>✓ Online Training</li><li>✓ Blog</li><li>✓ Contact</li></ul></div>
  <div class="col" style="left:450px"><h4>Our services</h4><ul>
    <li>✓ Anxiety and Depression</li><li>✓ Anger Management</li><li>✓ Dating and Relationships</li><li>✓ Self Esteem</li><li>✓ Trauma inc. EMDR</li><li style="text-decoration:underline;font-size:10px;margin-left:22px">VIEW MORE</li></ul></div>
  <div class="col contact" style="left:680px"><h4>Contact Us</h4><ul>
    <li><span class="ico"></span>CALL US<br>0400 218 736</li>
    <li><span class="ico"></span>FAX<br>(07) 3000 4821</li>
    <li><span class="ico"></span>24 Marlin Parade, Seabrook</li></ul></div>
  <div class="col" style="left:938px"><h4>Our Newsletter</h4>
    <p style="width:200px;line-height:15px">Subscribe our newsletter to get the latest news.</p>
    <div class="field"></div><div class="sub-btn">SUBSCRIBE</div></div>
</footer>

<div class="abs bottom">
  <span style="position:absolute;left:68px;top:30px">© Copyright 2023 Tolvenra</span>
  <div class="social"><i></i><i></i><i></i><i></i></div>
</div>

</body>
</html>
```